Super Greens Label for Supplement Bottle

We want to design a front label for a health supplement bottle. The product is called Meadow Twist Chews™. This will be a new product so there is no current website for the product. The focus is on supergreens that taste great and deliver support for energy, digestion, and immune defense.
We want it to be modern, vibrant and appealing.
Bottle size: standard size supplement CLEAR bottle size, with white child resistant cap and the label panel dimensions are 3” x 7”. The label should be primarily white and green, with a touch of red; (see color palettes)/it can also ONLY be white and green. See samples attached.
We are only focused on the front of the bottle design, not on the back, but leave space for the supplement panel and other text on the back.
So the text for the front of the bottle is:
RT Balden's
Meadow Twist Chews™
Super Greens Blend for:
Energy, Digestion, and Immune Support*
60 Gummies | Dietary Supplement
Raspberry Flavor Gummies
Off to side of the label:
Non-GMO
Vegan Friendly
Plant-Based
Gelatin Free
Colors
Designer to choose colors to be used in the design.

```html
<!DOCTYPE html>
<html lang="en">
<head>
<meta charset="utf-8">
<title>Meadow Twist Chews – Front Label</title>
<link href="https://fonts.googleapis.com/css2?family=Open+Sans:wght@700;800&family=Oswald:wght@500&display=swap" rel="stylesheet">
<style>
  :root {
    --green-deep: #0f7a34;
    --green-main: #2f9e3a;
    --green-light: #5cc04a;
    --letter-grey: #dcdcdc;
    --white: #ffffff;
    --ink: #222222;
    --berry: #d8334f;
    --berry-dark: #a81f38;
  }
  html, body { margin: 0; padding: 0; overflow: hidden; }
  body { width: 1134px; height: 1200px; background: var(--white); }
  .label { position: relative; width: 1134px; height: 1200px; overflow: hidden; background: var(--white); }

  .hero {
    position: absolute; left: 0; top: 0; width: 1134px; height: 700px; overflow: hidden;
    background: radial-gradient(circle at 75% 40%, var(--green-light), var(--green-main) 55%, #238a30 100%);
  }
  .veggie-art {
    position: absolute; right: 0; top: 0; width: 420px; height: 640px;
    background: radial-gradient(ellipse at 60% 45%, rgba(255,255,255,0.18), rgba(255,255,255,0) 70%);
  }
  .claim-strip {
    position: absolute; left: 0; top: 30px; width: 46px; height: 640px;
    background: var(--white); border-radius: 0 24px 24px 0;
  }
  .claim {
    position: absolute; left: 6px; width: 32px; height: 130px;
    border: 3px solid var(--green-main); border-radius: 16px; box-sizing: border-box;
    display: flex; align-items: center; justify-content: center;
  }
  .claim span {
    writing-mode: vertical-rl; transform: rotate(180deg);
    font: 500 13px/1 "Oswald", sans-serif; color: var(--green-main); white-space: nowrap;
  }
  .brand {
    position: absolute; left: 70px; top: 120px; margin: 0;
    font: 700 58px/1 "Open Sans", sans-serif; color: var(--white);
  }
  .name { margin: 0; font-family: "Open Sans", sans-serif; font-weight: 800; }
  .name .initial {
    position: absolute; left: 62px; top: 280px;
    font-size: 470px; line-height: 1; color: var(--letter-grey); letter-spacing: -10px;
  }
  .name .word {
    position: absolute; left: 500px; font-size: 150px; line-height: 1; color: var(--white); letter-spacing: -3px;
  }
  .name .tm { font-size: 50px; vertical-align: top; letter-spacing: 0; }
  .w1 { top: 285px; } .w2 { top: 425px; } .w3 { top: 575px; }

  .benefits-title {
    position: absolute; left: 95px; top: 735px; margin: 0;
    font: 500 44px/1 "Oswald", sans-serif; color: var(--ink);
  }
  .tree { position: absolute; left: 0; top: 0; }
  .benefit {
    position: absolute; text-align: center; width: 220px;
    font: 500 34px/1.15 "Oswald", sans-serif; color: var(--ink);
  }
  .raspberry {
    position: absolute; left: 770px; top: 780px; width: 270px; height: 220px;
    background: radial-gradient(ellipse at 50% 55%, var(--berry) 0%, var(--berry-dark) 45%, rgba(255,255,255,0) 72%);
  }
  .flavor {
    position: absolute; left: 770px; top: 1005px; width: 270px; margin: 0; text-align: center;
    font: 500 28px/1 "Oswald", sans-serif; color: var(--berry-dark);
  }
  .bottom { position: absolute; left: 0; top: 0; }
  .count {
    position: absolute; left: 95px; top: 1075px; display: flex; align-items: center; gap: 10px;
    color: var(--white); font-family: "Oswald", sans-serif; font-weight: 500;
  }
  .count .num { font-size: 100px; line-height: 1; }
  .count .unit { font-size: 42px; line-height: 1.05; }
  .supplement {
    position: absolute; left: 650px; top: 1090px; margin: 0;
    font: 500 42px/1 "Oswald", sans-serif; color: var(--ink);
  }
</style>
</head>
<body>
<div class="label">
  <section class="hero">
    <div class="veggie-art" role="img" aria-label="Line drawings of carrot, broccoli and leafy vegetables"></div>
    <div class="claim-strip">
      <div class="claim" style="top:15px"><span>NON-GMO</span></div>
      <div class="claim" style="top:170px"><span>VEGAN FRIENDLY</span></div>
      <div class="claim" style="top:325px"><span>PLANT-BASED</span></div>
      <div class="claim" style="top:480px"><span>GELATIN FREE</span></div>
    </div>
    <p class="brand">RT Balden's</p>
    <h1 class="name">
      <span class="initial">M</span>
      <span class="word w1">eadow</span>
      <span class="word w2">Twist</span>
      <span class="word w3">Chews<span class="tm">™</span></span>
    </h1>
  </section>

  <h2 class="benefits-title">SUPER GREENS BLEND FOR</h2>
  <svg class="tree" width="1134" height="1200" viewBox="0 0 1134 1200" fill="none" stroke-linecap="round" stroke-linejoin="round">
    <g stroke="var(--ink)" stroke-width="3">
      <path d="M110 800 H545 M110 800 V825 M300 800 V825 M545 800 V825"/>
    </g>
    <g stroke="var(--green-main)" stroke-width="5">
      <path d="M118 840 L98 885 H120 L102 930"/>
      <path d="M285 840 H320 Q332 852 320 864 H284 Q272 876 284 888 H320 Q332 900 320 912 H300 V935"/>
      <path d="M545 838 L585 852 V885 Q585 915 545 935 Q505 915 505 885 V852 Z"/>
      <path d="M545 868 V904 M527 886 H563"/>
    </g>
  </svg>
  <div class="benefit" style="left:5px; top:960px">ENERGY</div>
  <div class="benefit" style="left:195px; top:960px">DIGESTION</div>
  <div class="benefit" style="left:440px; top:960px">IMMUNE<br>SUPPORT</div>

  <div class="raspberry" role="img" aria-label="Photo of two raspberries with leaves"></div>
  <p class="flavor">RASPBERRY FLAVOR</p>

  <svg class="bottom" width="1134" height="1200" viewBox="0 0 1134 1200">
    <path fill="var(--green-deep)" d="M0 1200 V1050 H40 Q40 1060 70 1060 H470 Q500 1060 508 1090 L518 1140 Q525 1165 555 1165 H1134 V1200 Z"/>
  </svg>
  <div class="count"><span class="num">60</span><span class="unit">VEGAN<br>GUMMIES</span></div>
  <p class="supplement">DIETARY SUPPLEMENT</p>
</div>
</body>
</html>
```